Book Cover for Cyber Compliance Book

I need to get a book cover designed for use on "Pagewell Print Portal" - template attached.

The name of the book is: Charting KELMOR

Tagline: A Boardroom Leader’s Field Guide to Oversight and Endurance

Author: Martin J Hollis

Photo of author is attached and a logo for the QBWLN publishing organisation.

Please note: the author is high profile in the cyber security industry and use of his image and name on the book will help online sales.

I am open to changing the amount of copy used on the front and back of the book.

The book is about a European regulation for the financial sector called DORA Digital Operational Resilience Act. It is aimed at corporate level executives within the financial sector and the imagery should include relevant elements such as the EU, Financial sector, digital operations and cybersecurity.

I want to find an imaginative designer than can create something special and appealing.

I am not clear on exactly how many pages will be in the book so the template details may change slightly as the number becomes clear for the width of the spine etc. I will require all the template files used so I can make minor edits in AI or Photoshop

Note I can get the photo and attached logo in higher resolution if required

If possible I would like to see a 3D mockup of the book

Synopsis of Book:

n the ever-evolving landscape of financial services, the Digital Operational Resilience Act (DORA) stands as a beacon of change, ushering in a new era of regulatory requirements aimed at fortifying the digital fortitude of the sector. “Charting KELMOR: A Boardroom Leader’s Field Guide to Oversight and Endurance” is an indispensable guide tailored for leaders who are steering their organisations through the complexities of DORA compliance.
This comprehensive manual delves into the intricacies of DORA, elucidating the rationale behind its inception – the need for a unified and robust approach to managing ICT risks that have become increasingly prevalent in today’s interconnected financial ecosystem. The book offers a granular analysis of the five pillars central to DORA: ICT Risk Management, ICT-related Incident Management, Digital Operational Resilience Testing, ICT Third Party Risk Management, and Information Sharing Arrangements.
For financial entities and ICT service providers operating within the EU and beyond, “Charting KELMOR” serves as a strategic compass. It provides actionable insights into aligning with DORA’s standards, ensuring not just compliance but also a competitive edge in the EU market. The guide highlights the strategic importance of continuous learning and the emergence of specialized roles such as DORA Compliance Specialists, addressing the skills gap and career opportunities within this new regulatory framework.
The book also offers a detailed walkthrough of the Union-wide Oversight Framework, a novel aspect of DORA that places critical ICT third-party providers under direct regulatory scrutiny. It outlines the necessary steps for financial entities to ensure seamless collaboration with these providers, including the integration of specific contractual obligations to uphold DORA’s stringent resilience standards.
With practical advice and real-world scenarios, “Charting KELMOR” equips executives with the knowledge to conduct thorough DORA Compliance Assessments, map dependencies, and engage in scenario testing that aligns with the act’s rigorous testing regimen. It is not just a guide but a strategic tool for proactive adaptation and evolution in the face of DORA’s demands.
As the financial sector navigates these new regulatory waters, “Charting KELMOR” emerges as the quintessential guide for those committed to not just surviving but thriving in the age of digital operational resilience. It is a clarion call for attentiveness, alignment, and preparedness – a must-read for every financial service executive determined to lead their organization with foresight and fortitude.

```html
<!DOCTYPE html>
<html lang="en">
<head>
<meta charset="utf-8">
<title>Charting KELMOR – Book Cover Wrap</title>
<link rel="stylesheet" href="https://fonts.googleapis.com/css2?family=Montserrat:wght@400;500;600;700;800&family=Oswald:wght@600&display=swap">
<style>
  :root {
    --navy-deep: #06124a;
    --navy: #0b2a86;
    --blue: #1a5fd0;
    --blue-bright: #2fa6f2;
    --cyan-glow: #3ad3f5;
    --gold-light: #ffe866;
    --gold: #f2b807;
    --gold-dark: #b9760a;
    --white: #ffffff;
    --photo-top: #1d3f8f;
    --photo-bottom: #1a2540;
  }
  * { margin: 0; padding: 0; box-sizing: border-box; }
  html, body { width: 1200px; height: 866px; overflow: hidden; background: var(--navy-deep); }
  .cover-wrap {
    position: relative;
    width: 1200px; height: 866px;
    overflow: hidden;
    background:
      radial-gradient(ellipse 520px 380px at 930px 300px, rgba(58,211,245,0.45), transparent 70%),
      radial-gradient(ellipse 420px 300px at 260px 520px, rgba(47,166,242,0.35), transparent 70%),
      linear-gradient(180deg, var(--navy) 0%, var(--blue) 55%, var(--navy-deep) 100%);
    font-family: "Montserrat", sans-serif;
    color: var(--white);
  }
  .backdrop { position: absolute; inset: 0; }

  /* Back cover */
  .back-title {
    position: absolute; left: 50px; width: 482px; top: 34px;
    text-align: center; font-weight: 600; font-size: 24px; letter-spacing: 0.5px;
  }
  .back-blurb {
    position: absolute; left: 50px; top: 90px; width: 484px;
    font-size: 12.2px; line-height: 16px; font-weight: 500;
  }
  .barcode-space {
    position: absolute; left: 358px; top: 728px; width: 192px; height: 114px;
    background: var(--white);
  }

  /* Spine */
  .spine-title, .spine-author {
    position: absolute; writing-mode: vertical-rl; font-weight: 700; white-space: nowrap;
  }
  .spine-title { left: 586px; top: 52px; font-size: 23px; letter-spacing: 0.5px; }
  .spine-author { left: 590px; top: 646px; font-size: 19px; }

  /* Front cover */
  .front-title { position: absolute; left: 640px; width: 540px; top: 22px; text-align: center; }
  .front-title span {
    display: block;
    background: linear-gradient(180deg, var(--gold-light) 0%, var(--gold) 50%, var(--gold-dark) 100%);
    -webkit-background-clip: text; background-clip: text; color: transparent;
    filter: drop-shadow(2px 3px 2px rgba(0,0,0,0.55));
  }
  .title-line-1 { font-family: "Oswald", sans-serif; font-weight: 600; font-size: 104px; line-height: 112px; }
  .title-line-2 { font-weight: 800; font-size: 96px; line-height: 104px; letter-spacing: -2px; }
  .tagline {
    position: absolute; left: 660px; width: 504px; top: 248px;
    text-align: center; font-size: 22.5px; line-height: 23px; font-weight: 500;
    text-shadow: 0 1px 3px rgba(0,0,0,0.5);
  }
  .author-photo { position: absolute; left: 688px; top: 328px; width: 320px; height: 538px; }
  .author-name {
    position: absolute; left: 690px; width: 420px; top: 770px;
    text-align: center; font-weight: 700; font-size: 42px; letter-spacing: -0.5px;
    text-shadow: 2px 2px 4px rgba(0,0,0,0.8);
  }
  .publisher-mark {
    position: absolute; left: 1004px; top: 578px; width: 172px; height: 172px;
    border-radius: 50%;
    background: var(--navy-deep);
    border: 6px solid var(--white);
    display: flex; align-items: center; justify-content: center;
    font-weight: 700; font-size: 30px; letter-spacing: 2px;
  }
</style>
</head>
<body>
<div class="cover-wrap">

  <svg class="backdrop" width="1200" height="866" viewBox="0 0 1200 866" aria-hidden="true">
    <g fill="#37c8f2" opacity="0.35">
      <rect x="0" y="430" width="18" height="160"/>
      <rect x="28" y="470" width="18" height="120"/>
      <rect x="622" y="438" width="20" height="160"/>
      <rect x="650" y="470" width="20" height="128"/>
      <rect x="1000" y="470" width="26" height="150"/>
      <rect x="1040" y="440" width="26" height="180"/>
      <rect x="1080" y="490" width="26" height="130"/>
      <rect x="1120" y="500" width="26" height="120"/>
    </g>
    <path d="M0 530 C120 600 220 700 340 620 S520 420 620 470 S820 520 900 500 S1100 520 1200 540"
          fill="none" stroke="#ffffff" stroke-width="1.6" opacity="0.85"/>
    <g stroke="#5fc6ff" stroke-width="1" opacity="0.35" fill="none">
      <path d="M0 700 L1200 700"/><path d="M0 740 L1200 740"/><path d="M0 790 L1200 790"/>
      <path d="M0 845 L1200 845"/>
      <path d="M200 866 L420 660"/><path d="M420 866 L520 660"/><path d="M900 866 L820 660"/>
      <path d="M1100 866 L960 660"/>
    </g>
  </svg>

  <!-- Back cover -->
  <h2 class="back-title">Charting KELMOR</h2>
  <div class="back-blurb">
    <p>In the ever-evolving landscape of financial services, the Digital Operational Resilience Act (DORA) stands as a beacon of change, ushering in a new era of regulatory requirements aimed at fortifying the digital fortitude of the sector. “Charting KELMOR: A Boardroom Leader’s Field Guide to Oversight and Endurance” is an indispensable guide tailored for leaders who are steering their organisations through the complexities of DORA compliance. This comprehensive manual delves into the intricacies of DORA, elucidating the rationale behind its inception – the need for a unified and robust approach to managing ICT risks that have become increasingly prevalent in today’s interconnected financial ecosystem. The book offers a granular analysis of the five pillars central to DORA: ICT Risk Management, ICT-related Incident Management, Digital Operational Resilience Testing, ICT Third Party Risk Management, and Information Sharing Arrangements. For financial entities and ICT service providers operating within the EU and beyond, “Charting KELMOR” serves as a strategic compass. It provides actionable insights into aligning with DORA’s standards, ensuring not just compliance but also a competitive edge in the EU market. The guide highlights the strategic importance of continuous learning and the emergence of specialized roles such as DORA Compliance Specialists, addressing the skills gap and career opportunities within this new regulatory framework.</p>
    <p>The book also offers a detailed walkthrough of the Union-wide Oversight Framework, a novel aspect of DORA that places critical ICT third-party providers under direct regulatory scrutiny. It outlines the necessary steps for financial entities to ensure seamless collaboration with these providers, including the integration of specific contractual obligations to uphold DORA’s stringent resilience standards.</p>
    <p>With practical advice and real-world scenarios, “Charting KELMOR” equips executives with the knowledge to conduct thorough DORA Compliance Assessments, map dependencies, and engage in scenario testing that aligns with the act’s rigorous testing regimen. It is not just a guide but a strategic tool for proactive adaptation and evolution in the face of DORA’s demands.</p>
    <p>As the financial sector navigates these new regulatory waters, “Charting KELMOR” emerges as the quintessential guide for those committed to not just surviving but thriving in the age of digital operational resilience. It is a clarion call for attentiveness, alignment, and preparedness – a must-read for every financial service executive determined to lead their organization with foresight and fortitude.</p>
  </div>
  <div class="barcode-space"></div>

  <!-- Spine -->
  <div class="spine-title">Charting KELMOR</div>
  <div class="spine-author">Martin J Hollis</div>

  <!-- Front cover -->
  <h1 class="front-title">
    <span class="title-line-1">Charting</span>
    <span class="title-line-2">KELMOR</span>
  </h1>
  <p class="tagline">A Boardroom Leader’s Field Guide<br>to Oversight and Endurance</p>

  <svg class="author-photo" viewBox="0 0 320 538" role="img" aria-label="Portrait photograph of the author in a dark suit and red tie">
    <defs>
      <linearGradient id="photoTone" x1="0" y1="0" x2="0" y2="1">
        <stop offset="0" stop-color="var(--photo-top)" stop-opacity="0.35"/>
        <stop offset="0.5" stop-color="var(--photo-bottom)" stop-opacity="0.85"/>
        <stop offset="1" stop-color="var(--photo-bottom)"/>
      </linearGradient>
    </defs>
    <path d="M110 0 H220 Q250 0 250 60 V200 Q320 230 320 300 V538 H0 V300 Q0 230 70 200 V60 Q70 0 110 0 Z" fill="url(#photoTone)"/>
  </svg>

  <div class="publisher-mark">QBWLN</div>

  <div class="author-name">Martin J Hollis</div>
</div>
</body>
</html>
```